Physical Therapy Center for children Business Card

We need a Business Card for our company (Physical Therapy for children and youth with special needs) in Lisbon, Portugal. The name of the company is "Ninho de Luz"

The card must contain the following info:
- Logo: see uploaded file
- Name: Ninho de Luz
- Slogan: Plantamos carinho, colhemos risos, partilhamos conquistas!
- Service: Terapias Especializadas
- Address: Rua Henrique Lobato Farinha 9C
- ZipCode: 2741-318 Vale da Aurora
- E-mail: geral@velado.pt
- Site: www.velado.pt
- Facebook: www.facebook.com/ninhodeluz
- Phone: +351 21 584 62 07
- Cell Phone: +351 96 731 84 25

The stationary should have contain all info from business card.

Target Market(s)

Parents of children with special needs

Industry/Entity Type

Physical Therapy

Contact Information for Business Card

The card design should be compatible with http://www.quellprensa.com/product2/order_detail.php?gid=40

Requirements
Should not have
• The business card should not have a Black background. Use white or other color.

```html
<!DOCTYPE html>
<html lang="pt">
<head>
<meta charset="utf-8">
<title>Ninho de Luz — Cartão de Visita</title>
<link rel="stylesheet" href="https://fonts.googleapis.com/css2?family=Arimo:wght@400;700&display=swap">
<style>
  :root {
    --stage: #ececec;
    --coral: #e8443e;
    --sun: #f4c51f;
    --teal: #16ad98;
    --plum: #7b3f74;
    --paper: #ffffff;
    --ink-light: #ffffff;
  }
  * { box-sizing: border-box; margin: 0; padding: 0; }
  html, body {
    width: 1200px; height: 900px; overflow: hidden;
    background: var(--stage);
    font-family: "Arimo", Arial, sans-serif;
  }
  .stage {
    width: 1200px; height: 900px;
    display: flex; flex-direction: column; align-items: center; justify-content: center;
    gap: 48px;
  }
  .card {
    position: relative;
    width: 640px; height: 366px;
    border-radius: 22px;
    overflow: hidden;
    box-shadow: 0 8px 24px rgba(0,0,0,.15);
  }
  .brand-dot { flex: none; width: 22px; height: 22px; border-radius: 50%; background: var(--plum); }
  .brand-name { white-space: nowrap; font-weight: 700; }

  /* Front */
  .card-front { background: var(--coral); }
  .front-brand {
    position: absolute; left: 0; right: 0; top: 118px;
    display: flex; align-items: center; justify-content: center; gap: 14px;
  }
  .front-brand .brand-name { color: var(--ink-light); font-size: 40px; letter-spacing: .5px; }
  .slogan-strip {
    position: absolute; left: 0; right: 0; bottom: 36px;
    display: flex; align-items: center; gap: 10px;
  }
  .strip-bar { height: 12px; background: var(--sun); }
  .strip-bar.left { width: 96px; flex: none; }
  .strip-bar.right { flex: 1; }
  .slogan { color: var(--ink-light); font-size: 15px; white-space: nowrap; }

  /* Back */
  .card-back { background: var(--paper); }
  .back-brand {
    position: absolute; left: 30px; top: 166px; width: 222px;
    display: flex; align-items: center; gap: 10px;
  }
  .back-brand .brand-dot { width: 18px; height: 18px; }
  .back-brand .brand-name { color: var(--teal); font-size: 25px; line-height: 1; }
  .info-panel {
    position: absolute; left: 262px; right: 0; top: 40px; bottom: 72px;
    background: var(--plum);
    padding: 22px 26px;
    color: var(--ink-light);
  }
  .company { font-size: 22px; line-height: 1.1; }
  .service { color: var(--sun); font-size: 15px; margin-bottom: 8px; }
  .address { font-size: 14px; line-height: 1.35; margin-bottom: 10px; }
  .contacts { list-style: none; }
  .contacts li {
    display: flex; align-items: center; gap: 10px;
    color: var(--sun); font-size: 14px; line-height: 1.5;
  }
  .contacts svg { width: 12px; height: 12px; flex: none; }
  .contacts svg * { fill: none; stroke: var(--sun); stroke-width: 1.6; }
</style>
</head>
<body>
<main class="stage">

  <section class="card card-front" aria-label="Frente do cartão">
    <div class="front-brand">
      <span class="brand-dot"></span>
      <span class="brand-name">Ninho de Luz</span>
    </div>
    <div class="slogan-strip">
      <span class="strip-bar left"></span>
      <span class="slogan">Plantamos carinho, colhemos risos, partilhamos conquistas!</span>
      <span class="strip-bar right"></span>
    </div>
  </section>

  <section class="card card-back" aria-label="Verso do cartão">
    <div class="back-brand">
      <span class="brand-dot"></span>
      <span class="brand-name">Ninho de Luz</span>
    </div>
    <div class="info-panel">
      <p class="company">Ninho de Luz</p>
      <p class="service">Terapias Especializadas</p>
      <p class="address">Rua Henrique Lobato Farinha 9C<br>2741-318 Vale da Aurora</p>
      <ul class="contacts">
        <li>
          <svg viewBox="0 0 12 12" aria-hidden="true"><path d="M2 1.5l2 .3.8 2.4-1.2.9a6 6 0 0 0 3.3 3.3l.9-1.2 2.4.8.3 2c-4.8.5-9-3.7-8.5-8.5z"/></svg>
          +351 21 584 62 07
        </li>
        <li>
          <svg viewBox="0 0 12 12" aria-hidden="true"><rect x="3" y="1" width="6" height="10" rx="1"/><path d="M5.3 9.2h1.4"/></svg>
          +351 96 731 84 25
        </li>
        <li>
          <svg viewBox="0 0 12 12" aria-hidden="true"><rect x="1" y="2.5" width="10" height="7" rx=".8"/><path d="M1.3 3l4.7 3.6L10.7 3"/></svg>
          geral@velado.pt
        </li>
        <li>
          <svg viewBox="0 0 12 12" aria-hidden="true"><circle cx="6" cy="6" r="4.8"/><path d="M1.2 6h9.6M6 1.2c-2.6 2.8-2.6 6.8 0 9.6M6 1.2c2.6 2.8 2.6 6.8 0 9.6"/></svg>
          www.velado.pt
        </li>
        <li>
          <svg viewBox="0 0 12 12" aria-hidden="true"><rect x="1.5" y="1.5" width="9" height="9" rx="1.5"/></svg>
          www.facebook.com/ninhodeluz
        </li>
      </ul>
    </div>
  </section>

</main>
</body>
</html>
```